Roofing company in Toronto, Canada needs a logo design and business card design

We need a business card and logo created for our company. Our company is "KMB Roofing" which provides roofing services for commercial and residential customers. We serve customers in the Greater Toronto Area (in Canada) thus the name KMB.

We want the logo and business card to be a modern design displaying professionalism and quality in the work. We would prefer rounded corners for the business cards but are open to other ideas. The cards should be pleasant and appealing to customers.

Target Market(s)

Commercial and Residential customers

Industry/Entity Type

Roofing

Contact Information for Business Card

Logo Text

KMB Roofing

Requirements
Nice to have
• Colours that are pleasing to the eye but at the same time should stand out from other business cards. If the design can incorporate the name of KMB Roofing and the actual concept of roofing that would be nice.
Should not have
• Do not want the business cards or logo to be childish looking. Need to look professionally designed.

```html
<!DOCTYPE html>
<html lang="en">
<head>
<meta charset="utf-8">
<title>KMB Roofing – Business Card</title>
<link rel="stylesheet" href="https://fonts.googleapis.com/css2?family=Lato:wght@400;700;900&display=swap">
<style>
  :root {
    --stage: #2f2f31;
    --card-dark: #0b0b0b;
    --card-light: #ffffff;
    --brand-red: #e8232a;
    --ink: #141414;
    --ink-soft: #2a2a2a;
    --white: #ffffff;
  }
  * { box-sizing: border-box; margin: 0; padding: 0; }
  html, body {
    width: 1200px; height: 880px; overflow: hidden;
    background: var(--stage);
    font-family: "Lato", Arial, sans-serif;
  }
  .stage {
    position: relative; width: 1200px; height: 880px;
  }
  .card {
    position: absolute; left: 267px;
    width: 665px; height: 380px;
    border-radius: 26px; overflow: hidden;
    box-shadow: 0 14px 30px rgba(0,0,0,.45);
  }
  .card--back { top: 40px; background: var(--card-dark); }
  .card--front { top: 460px; background: var(--card-light); }

  .brand {
    display: flex; align-items: center; gap: 14px;
    font-weight: 900; letter-spacing: .5px; line-height: 1;
  }
  .brand__mark { width: 22px; height: 22px; background: var(--brand-red); flex: none; }

  .card--back .brand {
    position: absolute; left: 50%; top: 50%;
    transform: translate(-50%, -50%);
    color: var(--white); font-size: 56px;
  }
  .card--back .brand__mark { width: 30px; height: 30px; }

  .front__band {
    position: absolute; right: 0; top: 0;
    width: 235px; height: 100%;
    background: var(--brand-red);
    clip-path: polygon(28% 0, 100% 0, 100% 100%, 0 100%);
  }
  .card--front .brand {
    position: absolute; left: 44px; top: 56px;
    color: var(--ink); font-size: 44px;
  }
  .contact-person { position: absolute; left: 46px; top: 168px; }
  .contact-person__name {
    font-weight: 900; font-size: 22px; color: var(--ink); letter-spacing: .3px;
  }
  .contact-person__role {
    font-weight: 400; font-size: 17px; color: var(--brand-red); margin-top: 2px;
  }
  .contact-list {
    position: absolute; left: 46px; top: 238px;
    list-style: none;
  }
  .contact-list__item {
    display: flex; align-items: center; gap: 10px;
    font-size: 17px; color: var(--ink-soft); height: 27px;
  }
  .contact-list__icon {
    width: 20px; height: 20px; background: var(--brand-red);
    display: flex; align-items: center; justify-content: center; flex: none;
  }
  .contact-list__icon svg { width: 14px; height: 14px; }
</style>
</head>
<body>
<main class="stage">
  <section class="card card--back" aria-label="Business card, back">
    <div class="brand"><span class="brand__mark"></span><span class="brand__name">KMB Roofing</span></div>
  </section>

  <section class="card card--front" aria-label="Business card, front">
    <div class="front__band"></div>
    <div class="brand"><span class="brand__mark"></span><span class="brand__name">KMB Roofing</span></div>
    <div class="contact-person">
      <p class="contact-person__name">DANIEL REEVES</p>
      <p class="contact-person__role">Managing Director</p>
    </div>
    <ul class="contact-list">
      <li class="contact-list__item">
        <span class="contact-list__icon"><svg viewBox="0 0 24 24" fill="#fff"><path d="M6.6 10.8a15 15 0 0 0 6.6 6.6l2.2-2.2c.3-.3.7-.4 1-.2 1.1.4 2.3.6 3.6.6.6 0 1 .4 1 1V20c0 .6-.4 1-1 1A17 17 0 0 1 3 4c0-.6.4-1 1-1h3.5c.6 0 1 .4 1 1 0 1.3.2 2.5.6 3.6.1.3 0 .7-.2 1z"/></svg></span>
        (416) 555 0142
      </li>
      <li class="contact-list__item">
        <span class="contact-list__icon"><svg viewBox="0 0 24 24" fill="#fff"><path d="M7 3h10v5H7zM4 9h16a1 1 0 0 1 1 1v7h-4v4H7v-4H3v-7a1 1 0 0 1 1-1zm5 7v3h6v-3z"/></svg></span>
        (416) 555 0187
      </li>
      <li class="contact-list__item">
        <span class="contact-list__icon"><svg viewBox="0 0 24 24" fill="#fff"><path d="M3 5h18v14H3zm2 2v.5l7 5 7-5V7zm0 3v7h14v-7l-7 5z"/></svg></span>
        info@kmbroofing.ca
      </li>
      <li class="contact-list__item">
        <span class="contact-list__icon"><svg viewBox="0 0 24 24" fill="none" stroke="#fff" stroke-width="2"><circle cx="12" cy="12" r="9"/><path d="M3 12h18M12 3c3 3 3 15 0 18M12 3c-3 3-3 15 0 18"/></svg></span>
        www.kmbroofing.ca
      </li>
    </ul>
  </section>
</main>
</body>
</html>
```